American pesto sauce company needs a vintage/ old fashioned package design

Company name: Marisol Grove.
We need a food label design for 4 different flavors of pesto sauce: classic almond, sundried tomato, roasted red pepper, and Cajun spice. For those that do not know what pesto is, it is a sauce like tomato sauce that is traditionally Italian and goes on pasta or whatever you choose to put it on and the consistent ingredients are garlic, cheese, nuts, olive oil and basil. They are fresh, all natural without preservatives, artificial flavors or colors.
The design of the jar is an old fashioned wire bale jar used for preserving foods ( attached is a picture). I'm looking for a label with:
• an upscale vintage feel but will also stand out on a grocery store shelf. I have attached an example of the feel I am looking for as well as the format of the words with my company name.
• The word "Pesto" must be prominent on the label.
• metalic gold boarders that go around the whole label maybe with gold embellishments if you see fit for that upscale feeling.
• Also, as you can see in the attachment, there are different typesets. And it must be easy to read from at least 3 feet away.
• Each label will have a different color corresponding to the flavor- could be part of the flavor text
• The bottom of the front panel must have “Net Wt. 5.75 oz (162g)” in a creative format how you see fit. Measures: height-28 mm, width-75mm
• Need logo for top part of label with the letters MG for Marisol Grove and it will also contain the website, address and parent company name, use by date, etc. Measures:50 mm diameter
• The back panel of the label will contain the nutrition facts, ingredients and bar code. Measures: height-28 mm, width-75mm

Also the label is one piece with 3 different sections. Attached will be an example with measurements.
Updates

Check out this website on packaging. I absolutely love love love the Hartwell Pantry almond water labels. The colors for the different flavors. How its not just horizontal or vertical. The different typesets/fonts/typography. The flourishes and background thats faded.
http://brightwrapgallery.com/page/3/

Target Market(s)

Target market is medium- high income foodies between 35-65

Industry/Entity Type

Grocery Store

Requirements
Must have
• Net Wt on front lower panel. Separation of the company name Marisol & Pesto. See attachment.
Nice to have
• Name of flavor designed in a wave pattern as shown in attachment. Hand drawn font OK.

```html
<!DOCTYPE html>
<html lang="en">
<head>
<meta charset="utf-8">
<title>Marisol Grove Pesto – Jar Label Series</title>
<link rel="stylesheet" href="https://fonts.googleapis.com/css2?family=Alfa+Slab+One&family=Playfair+Display:ital,wght@1,900&family=Ultra&family=Source+Sans+3:wght@400;700&display=swap">
<style>
  :root{
    --page:#ffffff;
    --cream:#f7f1e3;
    --cream-deep:#efe6cf;
    --flourish:#e2d6bf;
    --ink:#4a3a30;
    --tomato:#c62127;
    --cajun:#f37021;
    --almond:#9fc5cc;
    --slate:#3f4a55;
    --tan:#bfa678;
    --pepper-green:#3b5a2a;
    --pepper-red:#e84a35;
    --charcoal:#4b4847;
  }
  *{box-sizing:border-box;margin:0;padding:0}
  html,body{width:1200px;height:1000px;overflow:hidden;background:var(--page)}
  .canvas{position:relative;width:1200px;height:1000px}

  .label{position:absolute;top:0;width:266px;height:1000px}
  .label--tomato{left:39px;--accent:var(--tomato);--strip:var(--tomato);--badge:var(--tomato);--brand:var(--tomato);--pesto:#6b2a1f;--heading:var(--tomato)}
  .label--cajun{left:323px;--accent:var(--cajun);--strip:var(--cajun);--badge:var(--cajun);--brand:var(--cajun);--pesto:var(--charcoal);--heading:var(--cajun)}
  .label--almond{left:609px;--accent:var(--almond);--strip:var(--almond);--badge:var(--almond);--brand:var(--slate);--pesto:var(--slate);--heading:var(--almond)}
  .label--pepper{left:896px;--accent:var(--pepper-red);--strip:var(--tan);--badge:var(--pepper-green);--brand:var(--pepper-green);--pesto:var(--pepper-red);--heading:var(--pepper-red)}

  /* back panel (printed upside down) */
  .back-panel{position:absolute;top:135px;left:0;width:266px;height:99px;background:var(--cream)}
  .back-panel__content{width:100%;height:100%;transform:rotate(180deg);padding:8px 10px;
    font-family:"Source Sans 3",sans-serif;font-size:4.6px;line-height:1.45;color:var(--ink)}
  .back-panel__title{font-family:"Alfa Slab One",serif;font-size:8px;color:var(--ink);letter-spacing:.3px;margin-bottom:5px}
  .back-panel__title em{font-family:"Playfair Display",serif;font-style:italic;font-weight:900;color:var(--heading);font-size:8.5px}
  .back-panel__title .star{color:var(--heading);margin:0 3px}
  .back-panel p{margin-bottom:3px}
  .back-panel b{font-weight:700}
  .back-panel__use-by{text-align:center;font-style:italic;margin-top:6px}

  /* connecting strip */
  .strip{position:absolute;left:123px;top:234px;width:20px;height:511px;background:var(--strip)}

  /* top seal */
  .seal{position:absolute;left:42px;top:399px;width:182px;height:182px}
  .seal .acc-fill{fill:var(--accent)}
  .seal .acc-stroke{stroke:var(--accent)}
  .seal .badge-fill{fill:var(--badge)}
  .seal text{font-family:"Source Sans 3",sans-serif}
  .seal__curve{font-size:5.2px;fill:var(--accent)}
  .seal__mark{font-family:"Alfa Slab One",serif !important;font-size:30px;fill:var(--accent)}
  .seal__name{font-family:"Alfa Slab One",serif !important;font-size:10.5px;fill:var(--ink)}
  .seal__ribbon-text{font-size:4.6px;font-weight:700;fill:#fff}
  .seal__small{font-size:4.3px;fill:var(--ink)}
  .seal__useby{font-size:4.6px;font-weight:700;fill:var(--accent)}

  /* front panel */
  .front-panel{position:absolute;top:745px;left:0;width:266px;height:98px;background:var(--cream);overflow:hidden}
  .front-panel__frame{position:absolute;inset:4px;border:1.5px solid var(--accent);opacity:.8}
  .front-panel__frame::after{content:"";position:absolute;inset:3px;border:1px dashed var(--accent);opacity:.7}
  .front-panel__flourish{position:absolute;left:14px;right:14px;top:12px;bottom:12px;
    background:radial-gradient(ellipse at 25% 55%,var(--flourish) 0,transparent 55%),
               radial-gradient(ellipse at 75% 55%,var(--flourish) 0,transparent 55%);opacity:.8}
  .front-panel__brand{position:absolute;top:5px;left:0;width:100%;text-align:center;
    font-family:"Alfa Slab One",serif;font-size:13px;letter-spacing:.5px;color:var(--brand)}
  .front-panel__badge{position:absolute;left:83px;top:23px;width:100px;height:48px;background:var(--badge);
    border-radius:16px/20px;box-shadow:inset 0 0 0 2px var(--badge),inset 0 0 0 3px var(--cream);
    display:flex;align-items:center;justify-content:center;text-align:center;
    font-family:"Playfair Display",serif;font-style:italic;font-weight:900;font-size:14px;line-height:1.05;color:var(--cream)}
  .front-panel__pesto{position:absolute;top:72px;left:0;width:100%;text-align:center;
    font-family:"Ultra",serif;font-size:15px;letter-spacing:1px;color:var(--pesto)}
  .front-panel__pesto span{font-size:8px;vertical-align:3px;margin:0 4px}
  .net-wt{position:absolute;left:33px;top:38px;width:22px;height:30px}
  .net-wt__disc{position:absolute;top:0;left:1px;width:20px;height:20px;border-radius:50%;background:var(--accent);
    color:#fff;font-family:"Source Sans 3",sans-serif;font-weight:700;font-size:5.5px;line-height:1.05;
    display:flex;flex-direction:column;align-items:center;justify-content:center}
  .label--almond .net-wt__disc,.label--almond .net-wt__tail{background:var(--slate)}
  .net-wt__tail{position:absolute;top:16px;width:6px;height:11px;background:var(--accent)}
  .net-wt__tail--l{left:5px;transform:skewX(12deg)}
  .net-wt__tail--r{right:5px;transform:skewX(-12deg)}
  .finest{position:absolute;left:192px;top:36px;transform:rotate(-14deg);text-align:center;
    font-family:"Alfa Slab One",serif;font-size:7.5px;line-height:1;color:var(--accent)}
  .label--almond .finest{color:var(--slate)}
  .finest small{display:block;font-size:7px}
</style>
</head>
<body>
<main class="canvas">

  <!-- Sundried Tomato -->
  <section class="label label--tomato">
    <div class="back-panel"><div class="back-panel__content">
      <div class="back-panel__title">MARISOL PESTO <span class="star">✱</span><em>Sundried Tomato</em></div>
      <p><b>Nutrition Facts</b> Serv. Size 1/4 Cup (63g) Amount Per Serving: <b>Calories</b> 220, Fat Cal. 170, <b>Total Fat</b> 19g (29% DV), Sat. Fat 3.5g (18% DV), <b>Cholest.</b> 5mg (2% DV), Sodium 280mg (12% DV), <b>Total Carb.</b> 8g (3% DV), Fiber 1g (4% DV), Sugars 4g, <b>Protein</b> 5g, Vitamin A (15% DV), Vitamin C (20% DV), Calcium (8% DV), Iron (6% DV). Based on a 2,000 calorie diet.</p>
      <p><b>Ingredients:</b> Extra Virgin Olive Oil, Sun-dried Tomatoes, Parmesan Cheese, Walnuts, Garlic, Basil, Sea Salt, Black Pepper.</p>
      <p><b>Contains:</b> Nuts and Cheese.</p>
      <p class="back-panel__use-by">Use or Freeze By Date on Jar</p>
    </div></div>
    <div class="strip"></div>
    <svg class="seal" viewBox="0 0 182 182" aria-label="Marisol Pesto seal">
      <circle cx="91" cy="91" r="90" fill="#f6efdc"/>
      <circle cx="91" cy="91" r="84" fill="none" class="acc-stroke" stroke-width="1.2"/>
      <circle cx="91" cy="91" r="79" fill="none" class="acc-stroke" stroke-width="7" opacity=".35" role="img" aria-label="ornamental lace border"/>
      <circle cx="91" cy="91" r="73" fill="#f9f4e6" class="acc-stroke" stroke-width="1"/>
      <ellipse cx="91" cy="66" rx="48" ry="24" fill="#e4d8c0" opacity=".7" role="img" aria-label="faded basil leaf flourish"/>
      <defs><path id="arc-tomato" d="M41 91 A50 50 0 0 1 141 91"/></defs>
      <text class="seal__curve"><textPath href="#arc-tomato" startOffset="50%" text-anchor="middle">Ready to eat. Keep refrigerated. OK to freeze.</textPath></text>
      <text class="seal__mark" x="91" y="88" text-anchor="middle">MG</text>
      <text class="seal__name" x="91" y="103" text-anchor="middle">MARISOL PESTO</text>
      <path class="badge-fill" d="M52 107 H130 L126 112 L130 117 H52 L56 112 Z"/>
      <text class="seal__ribbon-text" x="91" y="114" text-anchor="middle">ORLA FINE FOODS, LLC</text>
      <text class="seal__small" x="91" y="126" text-anchor="middle">4120 Alder St. Riverton, NY 10990</text>
      <text class="seal__small" x="91" y="132" text-anchor="middle">555-010-4287 · www.marisolgrove.com</text>
      <text class="seal__useby" x="91" y="142" text-anchor="middle">Use or Freeze by</text>
      <text class="seal__small" x="91" y="148" text-anchor="middle">DD/MM/YYYY</text>
    </svg>
    <div class="front-panel">
      <div class="front-panel__flourish" role="img" aria-label="faded vintage leaf flourishes"></div>
      <div class="front-panel__frame"></div>
      <div class="front-panel__brand">MARISOL</div>
      <div class="net-wt"><span class="net-wt__tail net-wt__tail--l"></span><span class="net-wt__tail net-wt__tail--r"></span><div class="net-wt__disc">4.5<span>OZ</span></div></div>
      <div class="front-panel__badge">Sundried<br>Tomato</div>
      <div class="finest">★FINEST★<small>MADE</small></div>
      <div class="front-panel__pesto"><span>●</span>PESTO<span>●</span></div>
    </div>
  </section>

  <!-- Cajun Spice -->
  <section class="label label--cajun">
    <div class="back-panel"><div class="back-panel__content">
      <div class="back-panel__title">MARISOL PESTO <span class="star">✱</span><em>Cajun Spice</em></div>
      <p><b>Nutrition Facts</b> Serv. Size 1/4 Cup (63g) Amount Per Serving: <b>Calories</b> 230, Fat Cal. 180, <b>Total Fat</b> 20g (31% DV), Sat. Fat 3.5g (18% DV), <b>Cholest.</b> 5mg (2% DV), Sodium 300mg (13% DV), <b>Total Carb.</b> 4g (1% DV), Fiber 1g (4% DV), Sugars 1g, <b>Protein</b> 5g, Vitamin A (10% DV), Calcium (8% DV), Iron (4% DV). Based on a 2,000 calorie diet.</p>
      <p><b>Ingredients:</b> Extra Virgin Olive Oil, Basil, Parmesan Cheese, Almonds, Garlic, Paprika, Cayenne Pepper, Sea Salt, Onion.</p>
      <p><b>Contains:</b> Nuts and Cheese.</p>
      <p class="back-panel__use-by">Use or Freeze By Date on Jar</p>
    </div></div>
    <div class="strip"></div>
    <svg class="seal" viewBox="0 0 182 182" aria-label="Marisol Pesto seal">
      <circle cx="91" cy="91" r="90" fill="#f6efdc"/>
      <circle cx="91" cy="91" r="84" fill="none" class="acc-stroke" stroke-width="1.2"/>
      <circle cx="91" cy="91" r="79" fill="none" class="acc-stroke" stroke-width="7" opacity=".35" role="img" aria-label="ornamental lace border"/>
      <circle cx="91" cy="91" r="73" fill="#f9f4e6" class="acc-stroke" stroke-width="1"/>
      <ellipse cx="91" cy="66" rx="48" ry="24" fill="#e4d8c0" opacity=".7" role="img" aria-label="faded basil leaf flourish"/>
      <defs><path id="arc-cajun" d="M41 91 A50 50 0 0 1 141 91"/></defs>
      <text class="seal__curve"><textPath href="#arc-cajun" startOffset="50%" text-anchor="middle">Ready to eat. Keep refrigerated. OK to freeze.</textPath></text>
      <text class="seal__mark" x="91" y="88" text-anchor="middle">MG</text>
      <text class="seal__name" x="91" y="103" text-anchor="middle">MARISOL PESTO</text>
      <path class="badge-fill" d="M52 107 H130 L126 112 L130 117 H52 L56 112 Z"/>
      <text class="seal__ribbon-text" x="91" y="114" text-anchor="middle">ORLA FINE FOODS, LLC</text>
      <text class="seal__small" x="91" y="126" text-anchor="middle">4120 Alder St. Riverton, NY 10990</text>
      <text class="seal__small" x="91" y="132" text-anchor="middle">555-010-4287 · www.marisolgrove.com</text>
      <text class="seal__useby" x="91" y="142" text-anchor="middle">Use or Freeze by</text>
      <text class="seal__small" x="91" y="148" text-anchor="middle">DD/MM/YYYY</text>
    </svg>
    <div class="front-panel">
      <div class="front-panel__flourish" role="img" aria-label="faded vintage leaf flourishes"></div>
      <div class="front-panel__frame"></div>
      <div class="front-panel__brand">MARISOL</div>
      <div class="net-wt"><span class="net-wt__tail net-wt__tail--l"></span><span class="net-wt__tail net-wt__tail--r"></span><div class="net-wt__disc">4.5<span>OZ</span></div></div>
      <div class="front-panel__badge">Cajun<br>Spice</div>
      <div class="finest">★FINEST★<small>MADE</small></div>
      <div class="front-panel__pesto"><span>●</span>PESTO<span>●</span></div>
    </div>
  </section>

  <!-- Classic Almond -->
  <section class="label label--almond">
    <div class="back-panel"><div class="back-panel__content">
      <div class="back-panel__title">MARISOL PESTO <span class="star">✱</span><em>Classic Almond</em></div>
      <p><b>Nutrition Facts</b> Serv. Size 1/4 Cup (63g) Amount Per Serving: <b>Calories</b> 240, Fat Cal. 200, <b>Total Fat</b> 22g (34% DV), Sat. Fat 4g (20% DV), <b>Cholest.</b> 5mg (2% DV), Sodium 260mg (11% DV), <b>Total Carb.</b> 3g (1% DV), Fiber 1g (4% DV), Sugars 0g, <b>Protein</b> 6g, Vitamin A (12% DV), Calcium (10% DV), Iron (4% DV). Based on a 2,000 calorie diet.</p>
      <p><b>Ingredients:</b> Extra Virgin Olive Oil, Basil, Almonds, Parmesan Cheese, Garlic, Sea Salt, Black Pepper.</p>
      <p><b>Contains:</b> Nuts and Cheese.</p>
      <p class="back-panel__use-by">Use or Freeze By Date on Jar</p>
    </div></div>
    <div class="strip"></div>
    <svg class="seal" viewBox="0 0 182 182" aria-label="Marisol Pesto seal">
      <circle cx="91" cy="91" r="90" fill="#f6efdc"/>
      <circle cx="91" cy="91" r="84" fill="none" class="acc-stroke" stroke-width="1.2"/>
      <circle cx="91" cy="91" r="79" fill="none" class="acc-stroke" stroke-width="7" opacity=".45" role="img" aria-label="ornamental lace border"/>
      <circle cx="91" cy="91" r="73" fill="#f9f4e6" class="acc-stroke" stroke-width="1"/>
      <ellipse cx="91" cy="66" rx="48" ry="24" fill="#e4d8c0" opacity=".7" role="img" aria-label="faded basil leaf flourish"/>
      <defs><path id="arc-almond" d="M41 91 A50 50 0 0 1 141 91"/></defs>
      <text class="seal__curve"><textPath href="#arc-almond" startOffset="50%" text-anchor="middle">Ready to eat. Keep refrigerated. OK to freeze.</textPath></text>
      <text class="seal__mark" x="91" y="88" text-anchor="middle">MG</text>
      <text class="seal__name" x="91" y="103" text-anchor="middle" style="fill:var(--slate)">MARISOL PESTO</text>
      <path class="badge-fill" d="M52 107 H130 L126 112 L130 117 H52 L56 112 Z"/>
      <text class="seal__ribbon-text" x="91" y="114" text-anchor="middle" style="fill:var(--slate)">ORLA FINE FOODS, LLC</text>
      <text class="seal__small" x="91" y="126" text-anchor="middle">4120 Alder St. Riverton, NY 10990</text>
      <text class="seal__small" x="91" y="132" text-anchor="middle">555-010-4287 · www.marisolgrove.com</text>
      <text class="seal__useby" x="91" y="142" text-anchor="middle">Use or Freeze by</text>
      <text class="seal__small" x="91" y="148" text-anchor="middle">DD/MM/YYYY</text>
    </svg>
    <div class="front-panel">
      <div class="front-panel__flourish" role="img" aria-label="faded vintage leaf flourishes"></div>
      <div class="front-panel__frame"></div>
      <div class="front-panel__brand">MARISOL</div>
      <div class="net-wt"><span class="net-wt__tail net-wt__tail--l"></span><span class="net-wt__tail net-wt__tail--r"></span><div class="net-wt__disc">4.5<span>OZ</span></div></div>
      <div class="front-panel__badge">Classic<br>Almond</div>
      <div class="finest">★FINEST★<small>MADE</small></div>
      <div class="front-panel__pesto"><span>●</span>PESTO<span>●</span></div>
    </div>
  </section>

  <!-- Roasted Red Pepper -->
  <section class="label label--pepper">
    <div class="back-panel"><div class="back-panel__content">
      <div class="back-panel__title">MARISOL PESTO <span class="star">✱</span><em>Roasted Red Pepper</em></div>
      <p><b>Nutrition Facts</b> Serv. Size 1/4 Cup (63g) Amount Per Serving: <b>Calories</b> 210, Fat Cal. 160, <b>Total Fat</b> 18g (28% DV), Sat. Fat 3g (15% DV), <b>Cholest.</b> 5mg (2% DV), Sodium 270mg (11% DV), <b>Total Carb.</b> 6g (2% DV), Fiber 1g (4% DV), Sugars 3g, <b>Protein</b> 5g, Vitamin A (25% DV), Vitamin C (60% DV), Calcium (8% DV). Based on a 2,000 calorie diet.</p>
      <p><b>Ingredients:</b> Roasted Red Peppers, Extra Virgin Olive Oil, Almonds, Parmesan Cheese, Garlic, Basil, Sea Salt, Black Pepper.</p>
      <p><b>Contains:</b> Nuts and Cheese.</p>
      <p class="back-panel__use-by">Use or Freeze By Date on Jar</p>
    </div></div>
    <div class="strip"></div>
    <svg class="seal" viewBox="0 0 182 182" aria-label="Marisol Pesto seal">
      <circle cx="91" cy="91" r="90" fill="#f6efdc"/>
      <circle cx="91" cy="91" r="84" fill="none" stroke="#bfa678" stroke-width="1.2"/>
      <circle cx="91" cy="91" r="79" fill="none" class="acc-stroke" stroke-width="7" opacity=".35" role="img" aria-label="ornamental lace border"/>
      <circle cx="91" cy="91" r="73" fill="#f9f4e6" stroke="#bfa678" stroke-width="1"/>
      <ellipse cx="91" cy="66" rx="48" ry="24" fill="#e4d8c0" opacity=".7" role="img" aria-label="faded basil leaf flourish"/>
      <defs><path id="arc-pepper" d="M41 91 A50 50 0 0 1 141 91"/></defs>
      <text class="seal__curve" style="fill:var(--pepper-green)"><textPath href="#arc-pepper" startOffset="50%" text-anchor="middle">Ready to eat. Keep refrigerated. OK to freeze.</textPath></text>
      <text class="seal__mark" x="91" y="88" text-anchor="middle">MG</text>
      <text class="seal__name" x="91" y="103" text-anchor="middle" style="fill:var(--pepper-red)">MARISOL PESTO</text>
      <path class="badge-fill" d="M52 107 H130 L126 112 L130 117 H52 L56 112 Z"/>
      <text class="seal__ribbon-text" x="91" y="114" text-anchor="middle">ORLA FINE FOODS, LLC</text>
      <text class="seal__small" x="91" y="126" text-anchor="middle">4120 Alder St. Riverton, NY 10990</text>
      <text class="seal__small" x="91" y="132" text-anchor="middle">555-010-4287 · www.marisolgrove.com</text>
      <text class="seal__useby" x="91" y="142" text-anchor="middle" style="fill:var(--pepper-green)">Use or Freeze by</text>
      <text class="seal__small" x="91" y="148" text-anchor="middle">DD/MM/YYYY</text>
    </svg>
    <div class="front-panel">
      <div class="front-panel__flourish" role="img" aria-label="faded vintage leaf flourishes"></div>
      <div class="front-panel__frame"></div>
      <div class="front-panel__brand">MARISOL</div>
      <div class="net-wt"><span class="net-wt__tail net-wt__tail--l"></span><span class="net-wt__tail net-wt__tail--r"></span><div class="net-wt__disc">4.5<span>OZ</span></div></div>
      <div class="front-panel__badge">Roasted<br>Red Pepper</div>
      <div class="finest">★FINEST★<small>MADE</small></div>
      <div class="front-panel__pesto"><span>●</span>PESTO<span>●</span></div>
    </div>
  </section>

</main>
</body>
</html>
```